Quorival Corporate Vision Mission Statement Infographic

We need an info graphic which summarizes and visually explains the companies Ambition Statement, Strategic Priorities, Principles and Brand Actions and how they relate to each other

```html
<!DOCTYPE html>
<html lang="en">
<head>
<meta charset="utf-8">
<title>Quorival — Principles and Brand Actions</title>
<link href="https://fonts.googleapis.com/css2?family=Jost:wght@300;400;600;700&display=swap" rel="stylesheet">
<style>
  :root {
    --navy: #3a5bab;
    --navy-dark: #2a3f7a;
    --ink: #1a1f36;
    --white: #ffffff;
    --excellence: #ebebf5;
    --excellence-band: #a9aab3;
    --compassion: #ff6a1a;
    --compassion-band: #c4501a;
    --independence: #3a5bab;
    --independence-band: #2c4585;
    --commitment: #00ad7a;
    --commitment-band: #00855a;
    --integrity: #7ba1d9;
    --integrity-band: #5a77a8;
    --map-light: #e6eaf2;
    --map-mid: #b9c6de;
  }
  html, body {
    margin: 0;
    padding: 0;
    width: 955px;
    height: 1200px;
    overflow: hidden;
    background: var(--white);
  }
  .infographic {
    display: block;
    width: 955px;
    height: 1200px;
    font-family: "Jost", "Futura", sans-serif;
  }
  .banner-face { fill: var(--navy); }
  .banner-tail { fill: var(--navy-dark); }
  .banner-title {
    fill: var(--white);
    font-weight: 600;
    font-size: 35px;
    letter-spacing: 0.5px;
  }
  .segment { stroke: var(--white); stroke-width: 10; stroke-linejoin: round; }
  .seg-excellence { fill: var(--excellence); }
  .band-excellence { fill: var(--excellence-band); }
  .seg-compassion { fill: var(--compassion); }
  .band-compassion { fill: var(--compassion-band); }
  .seg-independence { fill: var(--independence); }
  .band-independence { fill: var(--independence-band); }
  .seg-commitment { fill: var(--commitment); }
  .band-commitment { fill: var(--commitment-band); }
  .seg-integrity { fill: var(--integrity); }
  .band-integrity { fill: var(--integrity-band); }
  .hub { fill: var(--white); }

  .principle-kicker { font-size: 21px; font-weight: 300; text-anchor: middle; letter-spacing: 0.5px; }
  .principle-name { font-size: 29px; font-weight: 700; text-anchor: middle; letter-spacing: 0.5px; }
  .action-kicker { font-size: 19px; font-weight: 400; letter-spacing: 0.3px; }
  .action-value { font-size: 17px; font-weight: 600; }
  .on-light { fill: var(--ink); }
  .on-dark { fill: var(--white); }

  .icon-ring { fill: var(--white); }
  .footer-band { fill: var(--navy); }
  .footer-note { fill: var(--white); font-size: 24px; font-weight: 300; text-anchor: middle; }
  .download-icon { fill: none; stroke: var(--white); stroke-width: 5; stroke-linecap: round; stroke-linejoin: round; }
</style>
</head>
<body>
<svg class="infographic" viewBox="0 0 1000 1257" xmlns="http://www.w3.org/2000/svg" aria-labelledby="infographic-title">
  <defs>
    <filter id="ring-shadow" x="-20%" y="-20%" width="140%" height="140%">
      <feDropShadow dx="0" dy="4" stdDeviation="14" flood-color="#1a1f36" flood-opacity="0.12"/>
    </filter>
    <linearGradient id="map-fill" x1="0" y1="0" x2="1" y2="1">
      <stop offset="0" stop-color="var(--map-light)"/>
      <stop offset="1" stop-color="var(--map-mid)"/>
    </linearGradient>

    <path id="arc-excellence-outer" d="M381.9 496.3 A206 206 0 0 1 624.1 496.3"/>
    <path id="arc-excellence-inner" d="M398.4 519.0 A178 178 0 0 1 607.6 519.0"/>
    <path id="arc-compassion-outer" d="M624.1 496.3 A206 206 0 0 1 698.9 726.7"/>
    <path id="arc-compassion-inner" d="M607.6 519.0 A178 178 0 0 1 672.3 718.0"/>
    <path id="arc-integrity-outer" d="M307.1 726.7 A206 206 0 0 1 381.9 496.3"/>
    <path id="arc-integrity-inner" d="M333.7 718.0 A178 178 0 0 1 398.4 519.0"/>
    <path id="arc-independence-outer" d="M503 875 A212 212 0 0 0 704.6 728.5"/>
    <path id="arc-independence-inner" d="M503 849 A186 186 0 0 0 679.9 720.5"/>
    <path id="arc-commitment-outer" d="M301.4 728.5 A212 212 0 0 0 503 875"/>
    <path id="arc-commitment-inner" d="M326.1 720.5 A186 186 0 0 0 503 849"/>
  </defs>

  <!-- Title banner -->
  <g class="title-banner">
    <polygon class="banner-tail" points="160,85 240,85 240,140 160,140 180,112"/>
    <polygon class="banner-tail" points="840,85 760,85 760,140 840,140 820,112"/>
    <rect class="banner-face" x="195" y="65" width="610" height="58"/>
    <text id="infographic-title" class="banner-title" x="500" y="106" text-anchor="middle">PRINICPLES AND BRAND ACTIONS</text>
  </g>

  <!-- Principle wheel -->
  <g class="principle-wheel" filter="url(#ring-shadow)">
    <path class="segment seg-excellence" d="M276.7 351.5 A385 385 0 0 1 729.3 351.5 L592.3 540.0 A152 152 0 0 0 413.7 540.0 Z"/>
    <path class="segment seg-compassion" d="M729.3 351.5 A385 385 0 0 1 869.2 782.0 L647.6 710.0 A152 152 0 0 0 592.3 540.0 Z"/>
    <path class="segment seg-independence" d="M869.2 782.0 A385 385 0 0 1 503 1048 L503 815 A152 152 0 0 0 647.6 710.0 Z"/>
    <path class="segment seg-commitment" d="M503 1048 A385 385 0 0 1 136.8 782.0 L358.4 710.0 A152 152 0 0 0 503 815 Z"/>
    <path class="segment seg-integrity" d="M136.8 782.0 A385 385 0 0 1 276.7 351.5 L413.7 540.0 A152 152 0 0 0 358.4 710.0 Z"/>
  </g>
  <g class="action-bands">
    <path class="segment band-excellence" d="M366.6 475.3 A232 232 0 0 1 639.4 475.3 L592.3 540.0 A152 152 0 0 0 413.7 540.0 Z"/>
    <path class="segment band-compassion" d="M639.4 475.3 A232 232 0 0 1 723.7 734.7 L647.6 710.0 A152 152 0 0 0 592.3 540.0 Z"/>
    <path class="segment band-independence" d="M723.7 734.7 A232 232 0 0 1 503 895 L503 815 A152 152 0 0 0 647.6 710.0 Z"/>
    <path class="segment band-commitment" d="M503 895 A232 232 0 0 1 282.3 734.7 L358.4 710.0 A152 152 0 0 0 503 815 Z"/>
    <path class="segment band-integrity" d="M282.3 734.7 A232 232 0 0 1 366.6 475.3 L413.7 540.0 A152 152 0 0 0 358.4 710.0 Z"/>
  </g>
  <circle class="hub" cx="503" cy="663" r="150"/>

  <!-- Principle labels -->
  <g class="principle-label" transform="translate(503 373)">
    <text class="principle-kicker on-light" y="-5">PRINCIPLE:</text>
    <text class="principle-name on-light" y="30">EXCELLENCE</text>
  </g>
  <g class="principle-label" transform="translate(778.8 573.4) rotate(72)">
    <text class="principle-kicker on-light" y="-8">PRINCIPLE:</text>
    <text class="principle-name on-dark" y="24">COMPASSION</text>
  </g>
  <g class="principle-label" transform="translate(227.2 573.4) rotate(-72)">
    <text class="principle-kicker on-light" y="-8">PRINCIPLE:</text>
    <text class="principle-name on-dark" y="24">INTEGRITY</text>
  </g>
  <g class="principle-label" transform="translate(676.4 901.7) rotate(-36)">
    <text class="principle-kicker on-dark" y="-8">PRINCIPLE:</text>
    <text class="principle-name on-dark" y="24">INDEPENDENCE</text>
  </g>
  <g class="principle-label" transform="translate(329.6 901.7) rotate(36)">
    <text class="principle-kicker on-light" y="-8">PRINCIPLE:</text>
    <text class="principle-name on-dark" y="24">COMMITMENT</text>
  </g>

  <!-- Brand actions -->
  <g class="brand-action">
    <text class="action-kicker on-light"><textPath href="#arc-excellence-outer" startOffset="50%" text-anchor="middle">BRAND ACTION:</textPath></text>
    <text class="action-value on-dark"><textPath href="#arc-excellence-inner" startOffset="50%" text-anchor="middle">Embrace challenge</textPath></text>
  </g>
  <g class="brand-action">
    <text class="action-kicker on-light"><textPath href="#arc-compassion-outer" startOffset="50%" text-anchor="middle">BRAND ACTION:</textPath></text>
    <text class="action-value on-dark"><textPath href="#arc-compassion-inner" startOffset="50%" text-anchor="middle">Put people first</textPath></text>
  </g>
  <g class="brand-action">
    <text class="action-kicker on-light"><textPath href="#arc-integrity-outer" startOffset="50%" text-anchor="middle">BRAND ACTION:</textPath></text>
    <text class="action-value on-dark"><textPath href="#arc-integrity-inner" startOffset="50%" text-anchor="middle">Do the right thing</textPath></text>
  </g>
  <g class="brand-action">
    <text class="action-kicker on-light"><textPath href="#arc-independence-outer" startOffset="50%" text-anchor="middle">BRAND ACTION:</textPath></text>
    <text class="action-value on-dark"><textPath href="#arc-independence-inner" startOffset="50%" text-anchor="middle">Be extraordinary</textPath></text>
  </g>
  <g class="brand-action">
    <text class="action-kicker on-light"><textPath href="#arc-commitment-outer" startOffset="50%" text-anchor="middle">BRAND ACTION:</textPath></text>
    <text class="action-value on-dark"><textPath href="#arc-commitment-inner" startOffset="50%" text-anchor="middle">Go the extra mile</textPath></text>
  </g>

  <!-- Principle icons -->
  <g class="principle-icon" role="img" aria-label="Icon: person holding a flag, for Excellence">
    <circle class="icon-ring" cx="500" cy="243" r="70"/>
    <circle cx="500" cy="243" r="57" fill="var(--excellence)"/>
  </g>
  <g class="principle-icon" role="img" aria-label="Icon: presenter beside a rising chart, for Integrity">
    <circle class="icon-ring" cx="115" cy="515" r="70"/>
    <circle cx="115" cy="515" r="57" fill="var(--integrity)"/>
  </g>
  <g class="principle-icon" role="img" aria-label="Icon: two people exchanging, for Compassion">
    <circle class="icon-ring" cx="880" cy="535" r="70"/>
    <circle cx="880" cy="535" r="57" fill="var(--compassion)"/>
  </g>
  <g class="principle-icon" role="img" aria-label="Icon: runner with a briefcase, for Commitment">
    <circle class="icon-ring" cx="255" cy="970" r="70"/>
    <circle cx="255" cy="970" r="57" fill="var(--commitment)"/>
  </g>
  <g class="principle-icon" role="img" aria-label="Icon: winner on a podium, for Independence">
    <circle class="icon-ring" cx="740" cy="975" r="70"/>
    <circle cx="740" cy="975" r="57" fill="var(--independence)"/>
  </g>

  <!-- Footer -->
  <g class="footer">
    <rect class="footer-band" x="0" y="1155" width="1000" height="102"/>
    <rect x="82" y="1120" width="142" height="108" fill="url(#map-fill)" role="img" aria-label="Folded world map"/>
    <text class="footer-note" x="500" y="1208">Please read this entire brochure</text>
    <g class="download-icon" aria-label="Download">
      <path d="M905 1180 V1212"/>
      <path d="M893 1201 L905 1213 L917 1201"/>
      <path d="M887 1212 V1222 H923 V1212"/>
    </g>
  </g>
</svg>
</body>
</html>
```